Things the classroom never showd you

Things the classroom never showed you

"Unfiltered tips to help early career professionals successfully navigate the workplace"

I'VE INCLUDED LINKS TO SOME EXAMPLES OF COVERS THAT I LIKE.

Open to a creative concept. The book is sort of a guide for early career professionals and how they should navigate corporate America. Inside the book, I am giving tips on how to navigate work life. Most executive professionals have coaches, advisors and mentors to help them navigate the stressors of work. This is sort of a playbook for young professionals in the workplace.

Book Dimensions: 5.5" X 8.5"

Harvest Uprising
https://www.quillorbo.com/Harvest-Uprising-Spotting-Growing-Pleasing-ebook/dp/Q7TK42HW9Z/ref=sr_1_1?ie=UTF8&qid=2604417719&sr=8-1&keywords=harvest+uprising

The Compass Method: Find Your Purpose. Overcome Your Fear of Failure. Use Your Natural Talents And Strengths To Build A Successful Life. https://www.quillorbo.com/Compass-Method-Meaning-Abilities-Thriving-ebook/dp/Q4MW83RD2K/ref=pd_sim_351_11?_encoding=UTF8&psc=1&refRID=KDLL2PQAHB3ZMQFE71TC

Desk Exit Route: The 7 Steps to Build a Home Business, Quit your Job and Enjoy the Freedom: Includes Interviews of Paul Ray Vintner, Dave Marsh, Tim Halvey, Greg Dunmore, Anton Velikaris & others!
https://www.quillorbo.com/Desk-Exit-Route-Interviews-Velikaris-ebook/dp/Q2HC57NV31/ref=pd_sim_351_20?_encoding=UTF8&psc=1&refRID=MPBBRRFZ4KQDNSHV62AE

The Short Lunch Writing Map: The Solopreneur’s Guide to a Year’s Worth of Blog Post Ideas in 60 Minutes and Creating Content That Hooks and Sells
https://www.quillorbo.com/Short-Lunch-Writing-Map-Freelancers-ebook/dp/Q9VB26KS4L/ref=pd_sim_351_4_encoding=UTF8&psc=1&refRID=TG5RR22D7J4K816UW3PB

Crafting a Magnetic Landing Screen in Five Easy Moves: Your Blueprint to Website Home Page Content that Converts Visitors into Leads & Clients (Crafting a... Book 3)
https://www.quillorbo.com/Crafting-Magnetic-Landing-Easy-Moves-ebook/dp/Q3884PLMZD/ref=pd_sim_351_1?_encoding=UTF8&psc=1&refRID=WS6YYHTL4QMN7FD3ERBC

Target Market(s)

College Students- Early Career Professionals

Industry/Entity Type

School

Font styles to use
Serif

Colors

Designer to choose colors to be used in the design.

Requirements
Must have
• Diversity in the cover- something eye catching. Photo on back cover. I'VE INCLUDED LINKS TO SOME EXAMPLES OF COVERS THAT I LIKE
Nice to have
• Designers have the flexibility to exert their creativity.I'VE INCLUDED LINKS TO SOME EXAMPLES OF COVERS THAT I LIKE
Should not have
• My picture on the cover

```html
<!DOCTYPE html>
<html lang="en">
<head>
<meta charset="utf-8">
<title>Things the Classroom Never Showed You — Cover Wrap</title>
<link rel="stylesheet" href="https://fonts.googleapis.com/css2?family=Oswald:wght@500;600&family=Raleway:wght@700&family=Playfair+Display:wght@700&family=Reenie+Beanie&display=swap">
<style>
  :root {
    --stage: #9b9b9b;
    --green-edge: #7fbf98;
    --green-mid: #9fd09a;
    --green-glow: #d2e98f;
    --frame: #ffffff;
    --ink: #2b2b2b;
    --ink-soft: #3a3a3a;
    --paper: #f6f7f6;
    --note-pink: #efd3ea;
    --note-green: #d8ecd1;
    --note-yellow: #f3f0b5;
    --grid-tile: #e9eff5;
    --photo-hair: #7a4a26;
    --photo-jacket: #1e1e22;
  }
  * { box-sizing: border-box; margin: 0; padding: 0; }
  html, body { width: 1200px; height: 900px; overflow: hidden; }
  body { background: var(--stage); position: relative; }

  .cover {
    position: absolute;
    top: 70px;
    height: 760px;
    overflow: hidden;
    background: radial-gradient(ellipse at 55% 42%, var(--green-glow) 0%, var(--green-mid) 48%, var(--green-edge) 100%);
  }
  .cover--back { left: 88px; width: 492px; }
  .cover--spine { left: 580px; width: 40px; background: linear-gradient(90deg, var(--green-edge), var(--green-mid)); }
  .cover--front { left: 620px; width: 492px; }

  .cover__frame {
    position: absolute; inset: 14px;
    border: 4px solid var(--frame);
    pointer-events: none; z-index: 7;
  }

  .note {
    position: absolute;
    box-shadow: 2px 4px 8px rgba(0,0,0,.18);
    font-family: 'Reenie Beanie', cursive;
    color: var(--ink);
    line-height: 1.05;
  }
  .note--pink { background: var(--note-pink); }
  .note--green { background: var(--note-green); }
  .note--yellow { background: var(--note-yellow); }

  /* back */
  .blurb {
    position: absolute; left: 22px; top: 52px; width: 300px; height: 520px;
    background: var(--paper);
    transform: rotate(-3deg);
    box-shadow: 2px 4px 10px rgba(0,0,0,.15);
    padding: 26px 20px 0 24px;
    font-family: 'Reenie Beanie', cursive;
    color: var(--ink);
    z-index: 4;
  }
  .blurb__title { font-size: 40px; margin: 0 0 10px 30px; }
  .blurb__text { font-size: 21px; line-height: 1.05; margin-bottom: 18px; }
  .author-photo {
    position: absolute; right: 20px; bottom: 0; width: 200px; height: 380px;
    background: linear-gradient(180deg, var(--photo-hair) 0%, #a8734a 35%, var(--photo-jacket) 58%, var(--photo-jacket) 100%);
    border-radius: 100px 100px 0 0;
    z-index: 3;
  }
  .byline {
    position: absolute;
    font-family: 'Raleway', sans-serif; font-weight: 700;
    color: var(--ink-soft); letter-spacing: .5px;
  }
  .byline--back { left: 42px; bottom: 38px; font-size: 18px; z-index: 6; }

  /* spine */
  .spine__text {
    position: absolute; left: 50%; top: 50%;
    transform: translate(-50%, -50%) rotate(-90deg);
    white-space: nowrap;
    font-family: 'Oswald', sans-serif; font-weight: 600;
    font-size: 17px; letter-spacing: 2px; color: #fff;
  }
  .spine__author { font-family: 'Raleway', sans-serif; font-size: 9px; color: var(--ink-soft); margin-left: 40px; }

  /* front */
  .byline--front { left: 0; right: 0; top: 46px; text-align: center; font-size: 19px; }
  .title {
    position: absolute; left: 40px; right: 32px; top: 92px; height: 196px;
    font-family: 'Oswald', sans-serif; color: #fff;
    text-shadow: 2px 3px 4px rgba(0,0,0,.25);
  }
  .title__bracket { position: absolute; width: 60px; border: 4px solid #fff; }
  .title__bracket--left { left: 0; top: 0; border-right: none; border-bottom: none; height: 130px; }
  .title__bracket--right { right: 0; bottom: 0; border-left: none; border-top: none; height: 130px; }
  .title__row { position: absolute; left: 0; right: 0; display: flex; align-items: center; justify-content: center; gap: 8px; white-space: nowrap; }
  .title__row--one { top: 14px; }
  .title__row--two { top: 104px; }
  .title__big { font-size: 62px; font-weight: 600; line-height: 1; letter-spacing: -1px; }
  .title__small { font-size: 26px; font-weight: 500; line-height: .95; display: flex; flex-direction: column; }
  .subtitle {
    position: absolute; left: 30px; right: 30px; top: 304px; text-align: center;
    font-family: 'Playfair Display', serif; font-weight: 700;
    font-size: 13px; line-height: 1.45; color: var(--ink-soft); text-transform: uppercase;
  }
  .subtitle__rule { position: absolute; left: 50px; right: 40px; top: 352px; height: 3px; background: rgba(255,255,255,.7); }
  .dash-ring { position: absolute; left: 86px; top: 380px; }
  .grid-tile { position: absolute; background: var(--grid-tile); opacity: .85; }
  .grid-tile--left { left: 24px; bottom: 22px; width: 90px; height: 80px; clip-path: polygon(0 30%, 60% 0, 100% 40%, 100% 100%, 0 100%); }
  .grid-tile--right { right: 22px; bottom: 60px; width: 70px; height: 200px; clip-path: polygon(40% 0, 100% 10%, 100% 100%, 0 90%, 20% 40%); }
  .note__text { font-size: 28px; }
</style>
</head>
<body>

<section class="cover cover--back" aria-label="Back cover">
  <div class="blurb">
    <p class="blurb__title">Blurb Quote</p>
    <p class="blurb__text">Every page of this guide reads like advice from a mentor who has already walked the hallways you are just entering, honest and practical, with no fluff and no jargon.</p>
    <p class="blurb__text">Keep it on your desk for the first year of work and return to it whenever a meeting, a manager or a deadline feels bigger than you are.</p>
    <p class="blurb__text">A must read for anyone starting out in a new office.</p>
  </div>
  <div class="note note--green" style="left:330px;top:112px;width:84px;height:110px;transform:rotate(6deg);z-index:1"></div>
  <div class="note note--yellow" style="left:322px;top:236px;width:70px;height:130px;transform:rotate(4deg);z-index:1"></div>
  <div class="note note--pink" style="left:70px;top:540px;width:120px;height:110px;transform:rotate(-4deg);z-index:1"></div>
  <div class="author-photo" role="img" aria-label="Portrait photo of the author, smiling with arms crossed, wearing a dark blazer"></div>
  <p class="byline byline--back">MARISOL WHITCOMBE</p>
  <div class="cover__frame"></div>
</section>

<section class="cover cover--spine" aria-label="Spine">
  <p class="spine__text">THINGS THE CLASSROOM NEVER SHOWED YOU<span class="spine__author">MARISOL WHITCOMBE</span></p>
</section>

<section class="cover cover--front" aria-label="Front cover">
  <p class="byline byline--front">MARISOL WHITCOMBE</p>
  <h1 class="title">
    <span class="title__bracket title__bracket--left"></span>
    <span class="title__bracket title__bracket--right"></span>
    <span class="title__row title__row--one">
      <span class="title__small"><span>THINGS</span><span>THE</span></span>
      <span class="title__big">CLASSROOM</span>
    </span>
    <span class="title__row title__row--two">
      <span class="title__small"><span>NEVER</span></span>
      <span class="title__big">SHOWED</span>
      <span class="title__small"><span>YOU</span></span>
    </span>
  </h1>
  <p class="subtitle">Unfiltered tips to help early career professionals<br>successfully navigate the workplace</p>
  <div class="subtitle__rule"></div>

  <svg class="dash-ring" width="330" height="340" viewBox="0 0 330 340" aria-hidden="true">
    <ellipse cx="165" cy="170" rx="150" ry="150" fill="none" stroke="#fff" stroke-width="3" stroke-dasharray="18 14"/>
  </svg>

  <div class="grid-tile grid-tile--left" role="img" aria-label="Torn grid paper scrap"></div>
  <div class="grid-tile grid-tile--right" role="img" aria-label="Torn grid paper scrap"></div>

  <div class="note note--pink" style="left:34px;top:438px;width:180px;height:200px;transform:rotate(-9deg);padding:46px 20px 0 26px">
    <p class="note__text">The future<br>depends on<br>what you<br>do today!</p>
  </div>
  <div class="note note--green" style="left:292px;top:386px;width:178px;height:176px;transform:rotate(-3deg);padding:46px 10px 0 16px">
    <p class="note__text">Overcome your<br>fear of failure!</p>
  </div>
  <div class="note note--yellow" style="left:210px;top:560px;width:170px;height:166px;transform:rotate(-4deg);padding:46px 10px 0 14px">
    <p class="note__text" style="font-size:25px">Opportunities<br>don't happen,<br>you create them!</p>
  </div>
  <div class="cover__frame"></div>
</section>

</body>
</html>
```